Flyer need for startup recruiting company

Please see the instructions page here:

https://www.filevarro.com/scl/fo/k47pq2wxm93tzv8hn5lqd/h?rlkey=7vbnm3qsd82wcx4pl0yfr61kt&dl=0

```html
<!DOCTYPE html>
<html lang="en">
<head>
<meta charset="utf-8">
<title>TalentStrand – Advanced Sales Recruiting Flyer</title>
<link rel="stylesheet" href="https://fonts.googleapis.com/css2?family=Roboto:ital,wght@0,400;0,500;0,700;0,900;1,400;1,500&family=Roboto+Condensed:wght@400;500;700&display=swap">
<style>
  :root {
    --brand-blue: #1553a6;
    --deep-blue: #0d4694;
    --ink: #1d1d1f;
    --slate: #4d4f55;
    --tag-grey: #6a6d73;
    --stat-grey: #6c7077;
    --band-grey: #d5d6d8;
    --line-grey: #7d8188;
    --white: #ffffff;
  }
  * { box-sizing: border-box; margin: 0; padding: 0; }
  html, body { width: 950px; height: 1200px; overflow: hidden; background: #ececec; }
  body { font-family: "Roboto", Arial, sans-serif; color: var(--ink); }

  .flyer { position: relative; width: 950px; height: 1200px; background: var(--white); overflow: hidden; }

  /* Header */
  .brand { position: absolute; left: 44px; top: 50px; display: flex; align-items: center; gap: 12px; }
  .brand-dot { width: 38px; height: 38px; border-radius: 50%; background: var(--brand-blue); }
  .brand-text { display: flex; flex-direction: column; }
  .brand-name { font-weight: 700; font-size: 40px; line-height: 1; color: var(--brand-blue); letter-spacing: -0.5px; }
  .brand-tag { font-weight: 400; font-size: 19px; color: var(--tag-grey); margin-top: 2px; }

  .intro { position: absolute; left: 0; width: 520px; color: var(--white); padding: 0 45px; font-size: 14.4px; line-height: 19.2px; }
  .intro--about { top: 129px; height: 138px; background: var(--brand-blue); padding-top: 13px; font-weight: 400; }
  .intro--guarantee { top: 267px; height: 140px; background: var(--deep-blue); padding-top: 12px; font-weight: 500; }

  .value-band { position: absolute; left: 0; top: 407px; width: 950px; height: 110px; background: var(--band-grey); padding: 8px 45px 0; }
  .value-band h2 { font-weight: 900; font-size: 23px; color: var(--brand-blue); letter-spacing: -0.2px; }
  .value-band p { font-size: 13.8px; line-height: 19.2px; margin-top: 2px; }

  .hero { position: absolute; left: 0; top: 0; width: 950px; height: 530px; }

  /* Pricing */
  .pricing { position: absolute; left: 45px; top: 540px; width: 420px; }
  .section-title { font-weight: 900; font-size: 22.5px; color: var(--brand-blue); letter-spacing: -0.3px; }
  .levels { position: relative; margin-top: 4px; }
  .levels::before { content: ""; position: absolute; left: 9px; top: 14px; bottom: 6px; border-left: 2px dotted var(--brand-blue); }
  .level { position: relative; padding-left: 30px; margin-bottom: 17px; font-size: 15px; line-height: 20.4px; }
  .level::before { content: ""; position: absolute; left: 1px; top: 3px; width: 12px; height: 12px; border-radius: 50%; background: var(--stat-grey); border: 3px solid var(--white); box-shadow: 0 0 0 2px var(--brand-blue); }
  .level-name { font-weight: 700; font-size: 19px; color: var(--slate); line-height: 22px; }
  .level-role { font-weight: 700; font-size: 15px; color: var(--brand-blue); }
  .level-save { font-style: italic; font-weight: 500; }

  /* Right column */
  .savings { position: absolute; left: 488px; top: 540px; width: 412px; }
  .savings .section-title { font-size: 22.5px; line-height: 30px; }
  .bad-hire { font-weight: 700; font-size: 19px; margin-top: 8px; color: var(--ink); }
  .bad-hire-list { list-style: none; margin-top: 3px; font-size: 15px; line-height: 24px; }
  .bad-hire-list li { display: flex; align-items: center; gap: 8px; }
  .tick { width: 13px; height: 13px; flex: none; }
  .motto { font-weight: 700; font-size: 19px; text-align: center; line-height: 25px; margin-top: 9px; }
  .method { font-size: 14px; line-height: 19.2px; text-align: justify; margin-top: 4px; letter-spacing: -0.1px; }

  .stats { position: absolute; left: 488px; top: 886px; width: 416px; display: grid; grid-template-columns: 190px 214px; grid-template-rows: 66px 66px; gap: 9px 8px; }
  .stat { display: flex; align-items: center; gap: 8px; padding-left: 10px; color: var(--white); }
  .stat--blue { background: var(--deep-blue); }
  .stat--grey { background: var(--stat-grey); }
  .stat-figure { font-family: "Roboto Condensed", Arial, sans-serif; font-weight: 500; font-size: 27px; }
  .stat-label { font-size: 14.5px; line-height: 17px; }

  .closing { position: absolute; left: 488px; top: 1040px; width: 416px; font-size: 14px; line-height: 19.2px; text-align: justify; }

  /* Footer */
  .footer-shape { position: absolute; left: 0; bottom: 0; width: 950px; height: 80px; }
  .contact { position: absolute; left: 45px; bottom: 17px; display: flex; gap: 26px; color: var(--white); font-size: 18px; font-weight: 500; }
  .contact span { display: flex; align-items: center; gap: 8px; }
  .contact svg { width: 16px; height: 16px; }
</style>
</head>
<body>
<main class="flyer">

  <header class="brand">
    <span class="brand-dot"></span>
    <div class="brand-text">
      <span class="brand-name">TalentStrand</span>
      <span class="brand-tag">Advanced Sales Recruiting</span>
    </div>
  </header>

  <section class="intro intro--about">
    <p>TalentStrand is an advanced recruiting service<br>company that specializes in recruiting<br>professional sales people &amp; sales management<br>professionals using proven psychological<br>testing assessments that guarantee a top<br>performer 92% of the time.</p>
  </section>
  <section class="intro intro--guarantee">
    <p>Our ability to accurately source the top 10% of<br>sales candidates allows us to offer the BEST<br>guarantee in the recruiting industry. If our<br>recommended candidate does not become a top<br>performer within 6 month, we will replace that<br>candidate at no cost to you.</p>
  </section>

  <section class="value-band">
    <h2>THE BEST VALUE:</h2>
    <p>25 years of experience and <strong>flat rate pricing</strong>. Half the cost or more<br>of the traditional contingency model. Also, our 6 month guarantee<br>does not end with the 1st replacement so there is zero risk.</p>
  </section>

  <svg class="hero" viewBox="0 0 950 530">
    <defs>
      <linearGradient id="photo-tones" x1="0" y1="0" x2="1" y2="1">
        <stop offset="0" stop-color="#dfe6ec"/>
        <stop offset="0.55" stop-color="#c2ccd5"/>
        <stop offset="1" stop-color="#a9b2b9"/>
      </linearGradient>
    </defs>
    <path class="photo-ring" d="M447 0 C418 70 398 170 399 258 C400 345 440 425 528 468 C600 502 690 510 770 500 C850 488 905 450 950 416" fill="none" stroke="var(--deep-blue)" stroke-width="4"/>
    <path class="photo-area" d="M460 0 C432 70 408 170 409 258 C410 340 452 415 532 456 C600 490 690 496 765 486 C845 474 900 440 950 404 L950 0 Z" fill="url(#photo-tones)" stroke="var(--white)" stroke-width="5" role="img" aria-label="Photo of four smiling sales professionals seated at a meeting table with a laptop and papers"/>
  </svg>

  <section class="pricing">
    <h2 class="section-title">THERE ARE FIVE LEVELS OF PRICING</h2>
    <div class="levels">
      <article class="level">
        <h3 class="level-name">LEVEL 1</h3>
        <div class="level-role">B2C In home sales professionals</div>
        <p>Windows, roofs, solar, gutters, flooring etc<br>$6,000 with a two candidate retainer minimum<br><span class="level-save">Save $12,000 over contingency model ($18,000)</span></p>
      </article>
      <article class="level">
        <h3 class="level-name">LEVEL 2</h3>
        <div class="level-role">B2B Account Manger</div>
        <p>(80% Account Mgr, 20% Hunter Inside Sales, SaaS,<br>Outside sales, etc $12,000 with a two candidate<br>retainer minimum <span class="level-save">Save $13,000 over contingency<br>model ($25,000)</span></p>
      </article>
      <article class="level">
        <h3 class="level-name">LEVEL 3</h3>
        <div class="level-role">B2B Business Development Pro. Hunter</div>
        <p>$15,000 with a two candidate retainer minimum<br><span class="level-save">Save $15,000 over contingency model ($30,000)</span></p>
      </article>
      <article class="level">
        <h3 class="level-name">LEVEL 4</h3>
        <div class="level-role">B2B &amp; B2C Sales Mangers</div>
        <p>$17,000 with a one candidate retainer minimum<br><span class="level-save">Save $18,000 over contingency model ($35,000)</span></p>
      </article>
      <article class="level">
        <h3 class="level-name">LEVEL 5</h3>
        <div class="level-role">B2B &amp; B2C VP of Sales, CRO, CSO</div>
        <p>$19,000 with a one candidate retainer minimum<br><span class="level-save">Save $41,000 over contingency model ($60,000)</span></p>
      </article>
    </div>
  </section>

  <section class="savings">
    <h2 class="section-title">Save up to $200,000 hiring the right candidate</h2>
    <h3 class="bad-hire">Querra: The true cost of a bad hire</h3>
    <ul class="bad-hire-list">
      <li><svg class="tick" viewBox="0 0 14 14"><rect x="1" y="2" width="10" height="10" fill="none" stroke="var(--brand-blue)" stroke-width="1.6"/><path d="M3.5 7 L6 9.5 L12.5 2.5" fill="none" stroke="var(--brand-blue)" stroke-width="1.8"/></svg>4 X 1 year salary for front line workers</li>
      <li><svg class="tick" viewBox="0 0 14 14"><rect x="1" y="2" width="10" height="10" fill="none" stroke="var(--brand-blue)" stroke-width="1.6"/><path d="M3.5 7 L6 9.5 L12.5 2.5" fill="none" stroke="var(--brand-blue)" stroke-width="1.8"/></svg>10 X 1 year salary for sales pro’s</li>
      <li><svg class="tick" viewBox="0 0 14 14"><rect x="1" y="2" width="10" height="10" fill="none" stroke="var(--brand-blue)" stroke-width="1.6"/><path d="M3.5 7 L6 9.5 L12.5 2.5" fill="none" stroke="var(--brand-blue)" stroke-width="1.8"/></svg>20-24 X 1 year salary for sales leadership</li>
    </ul>
    <p class="motto">“Recruiting the BEST sales professionals is<br>in our DNA”</p>
    <p class="method">Our sourcing and vetting process is more advanced than the traditional, multi-job-function model. We only source the top 10% of sales professionals using an advanced psychological assessment process created by 16 psychologist &amp; has been used successfully on over 2.6 Million candidates since 1988.</p>
  </section>

  <section class="stats">
    <div class="stat stat--blue"><span class="stat-figure">50%</span><span class="stat-label">Faster time<br>to hire</span></div>
    <div class="stat stat--grey"><span class="stat-figure">83%</span><span class="stat-label">New hire retention<br>beyond the one year</span></div>
    <div class="stat stat--grey"><span class="stat-figure">96%</span><span class="stat-label">Of wrong hires<br>eliminated</span></div>
    <div class="stat stat--blue"><span class="stat-figure">50%</span><span class="stat-label">Lower employee<br>turnover</span></div>
  </section>

  <p class="closing">With 25+ years experience, we do the heavy lifting so you can focus on your core business. We do the sourcing, F2F screenings with sophisticated questions. We take the top 20% &amp; administer the advanced psychological assessment that is objective, highly predictive and benchmarked against 2.3 million sales people since 1998, You get our seal of approval that your candidate is in the top 10%.</p>

  <svg class="footer-shape" viewBox="0 0 950 80" preserveAspectRatio="none">
    <path d="M0 4 H462 Q470 4 473 11 L491 74 H950" fill="none" stroke="var(--line-grey)" stroke-width="4"/>
    <path d="M0 12 H452 Q458 12 461 18 L478 80 H0 Z" fill="var(--brand-blue)"/>
  </svg>
  <div class="contact">
    <span><svg viewBox="0 0 16 16"><circle cx="8" cy="8" r="7" fill="none" stroke="#fff" stroke-width="1.2"/><path d="M5.3 4.4 L6.6 4.2 L7.3 6 L6.5 6.8 Q7.2 8.4 8.9 9.4 L9.7 8.6 L11.5 9.3 L11.4 10.6 Q10.6 11.6 9 11 Q5.8 9.6 4.8 6.4 Q4.5 5 5.3 4.4 Z" fill="#fff"/></svg>555-310-0188</span>
    <span><svg viewBox="0 0 16 16"><circle cx="8" cy="8" r="7" fill="none" stroke="#fff" stroke-width="1.2"/><ellipse cx="8" cy="8" rx="3" ry="7" fill="none" stroke="#fff" stroke-width="1"/><path d="M1 8 H15 M2 4.8 H14 M2 11.2 H14" stroke="#fff" stroke-width="1"/></svg>www.TalentStrand.com</span>
  </div>

</main>
</body>
</html>
```